Healthy Food Healthy Brain Rack Card

We want a new 2 page (front and page) 3.67" x 8.5" rack card. This rack card is the first of a series we are creating. We will have five more eventually.

The minimum font size for the text on the front is 11 point and also for other main body text.

Use the text on the word document.

The images and layout in the word document are just sample ideas we had.

We have a subscripton to adobe stock images so prefer to get images from there or free high quality images.

The document is for older readers. Do not put text over graphics and keep it simple and easy to read with high contrast.

We are open to any color scheme, though something that conveys fresh and healthy, is good.

We want some very simple design element(s) incorporated that convey Native American communities or heritage. But NO head dress, teepee graphics, etc.

At the top, of the first page we would like a collage of healthy food images. This can include fish, chicken, fresh vegetables, berries, brown rice, etc.

On the back side, the text below the brown box on the word document with the title "mock up" can be smaller as needed.

Please remember to include the funding statement - it can be in a very small font 6/7 point.

For more information about our project, please visit https://velmorcollective.org/mind-care/

```html
<!DOCTYPE html>
<html lang="en">
<head>
<meta charset="utf-8">
<title>Healthy Food, Healthy Brain – Rack Card</title>
<link rel="stylesheet" href="https://fonts.googleapis.com/css2?family=Bebas+Neue&family=Barlow+Semi+Condensed:wght@400;500;600;700&family=Barlow+Condensed:wght@500;600;700&family=Montserrat:wght@700&family=Great+Vibes&display=swap">
<style>
  :root{
    --brown:#5f3006;
    --brown-text:#6b380c;
    --green:#8cc41f;
    --green-dark:#6f9a1d;
    --ink:#2b2b2b;
    --grey-text:#3d3d3d;
    --paper:#f4f4f2;
    --paper-shade:#e6e6e3;
    --white:#ffffff;
    --stage-top:#718f18;
    --stage-bottom:#486812;
  }
  *{margin:0;padding:0;box-sizing:border-box}
  html,body{width:1200px;height:1200px;overflow:hidden}
  body{
    background:linear-gradient(160deg,var(--stage-top),var(--stage-bottom));
    font-family:"Barlow Semi Condensed",sans-serif;
    position:relative;
  }
  .card{
    position:absolute;top:60px;width:466px;height:1080px;overflow:hidden;
    background:linear-gradient(90deg,var(--paper),#fbfbfa 30%,var(--paper) 60%,var(--paper-shade));
  }
  .card--front{left:100px}
  .card--back{left:633px}
  .abs{position:absolute}

  /* FRONT */
  .front-header{left:0;top:0;width:100%;height:196px;background:var(--brown)}
  .front-header__pointer{position:absolute;left:32px;bottom:-10px;width:0;height:0;
    border-left:9px solid transparent;border-right:9px solid transparent;border-top:10px solid var(--brown)}
  .front-title{position:absolute;left:0;top:0;width:466px;height:196px;display:block}
  .front-title text{font-family:"Bebas Neue",sans-serif;font-size:98px}
  .front-title__food{fill:var(--white)}
  .front-title__brain{fill:var(--green)}
  .intro{left:28px;top:262px;width:420px;font-size:17.5px;line-height:26px;color:var(--ink);text-align:justify}
  .steps-heading{left:34px;top:388px;font-family:"Montserrat",sans-serif;font-weight:700;font-size:17.5px;color:var(--brown-text)}
  .steps{left:34px;top:420px;list-style:none;width:410px}
  .steps li{position:relative;padding-left:39px;font-size:17.5px;line-height:26px;color:var(--grey-text);white-space:nowrap}
  .steps li svg{position:absolute;left:0;top:6px}
  .small-changes{left:36px;top:714px;font-family:"Barlow Condensed",sans-serif;font-weight:700;font-size:21px;line-height:31px;color:var(--ink)}
  .doctor-band{left:0;top:778px;width:100%;height:86px}
  .doctor-band__text{left:45px;top:795px;font-family:"Barlow Condensed",sans-serif;font-weight:700;font-size:20.5px;line-height:29px;color:var(--white);letter-spacing:.2px}
  .quote{left:26px;top:866px;width:430px;font-size:20px;line-height:30.5px;color:var(--ink)}
  .quote__mark{font-family:Georgia,serif;font-size:22px;font-weight:700;vertical-align:top}
  .quote p{padding-left:20px;white-space:nowrap}
  .quote cite{display:block;font-style:normal;padding-left:11px}
  .food-collage{left:0;top:955px;width:100%;height:125px;
    background:linear-gradient(90deg,#4d7a2c 0%,#e9a23a 18%,#8fa838 32%,#9a5a2e 48%,#c4312a 62%,#a8434c 74%,#ec8a52 86%,#e6c23f 100%)}

  /* BACK */
  .back-header{left:0;top:0;width:100%;height:112px;background:var(--brown)}
  .recipe-photo{left:23px;top:15px;width:139px;height:129px;
    background:linear-gradient(135deg,#c9ccd0,#9ea6ad 35%,#e5825f 60%,#b9bec3)}
  .back-title{left:178px;top:22px;font-family:"Barlow Condensed",sans-serif;font-weight:600;font-size:33px;line-height:1;color:var(--white);letter-spacing:.3px;white-space:nowrap}
  .back-subtitle{left:177px;top:58px;font-family:"Barlow Condensed",sans-serif;font-weight:500;font-size:20px;color:var(--green);white-space:nowrap}
  .ingredients-tag{left:174px;top:97px;width:122px;height:29px}
  .ingredients-tag span{position:absolute;left:0;top:0;width:100%;text-align:center;line-height:29px;
    font-family:"Barlow Condensed",sans-serif;font-weight:500;font-size:19px;color:var(--white)}
  .ingredients-arrow{left:282px;top:85px}
  .ingredient{position:absolute;font-family:"Barlow Condensed",sans-serif;font-weight:500;font-size:19px;line-height:22px;color:var(--brown-text);padding-left:19px;white-space:nowrap}
  .ingredient::before{content:"";position:absolute;left:0;top:8px;width:6px;height:6px;border-radius:50%;background:var(--green-dark)}
  .recipe-steps{left:20px;top:273px;width:426px;text-align:center;font-family:"Barlow Condensed",sans-serif;font-weight:500;font-size:20px;line-height:28.6px;color:var(--ink)}
  .careful{left:0;top:440px;width:100%;text-align:center;font-family:"Great Vibes",cursive;font-size:40px;color:var(--ink)}
  .community-box{left:0;top:497px;width:100%;height:159px;background:var(--brown);
    display:flex;align-items:center;justify-content:center;text-align:center;
    font-family:"Barlow Condensed",sans-serif;font-weight:500;font-size:21.5px;line-height:33.5px;color:var(--white)}
  .more-info{left:0;top:670px;width:100%;text-align:center;font-family:"Barlow Condensed",sans-serif;font-weight:600;font-size:41px;line-height:43px;color:var(--brown-text)}
  .site-pill{left:47px;top:761px;width:374px;height:36px;border-radius:18px;background:var(--brown);
    display:flex;align-items:center;justify-content:center;gap:7px;font-family:"Barlow Condensed",sans-serif;font-weight:500;font-size:18.5px;color:var(--white)}
  .resource-frame{left:52px;top:808px;width:364px;height:94px;border:1px solid var(--ink);border-bottom:none}
  .resource-frame__text{left:0;top:810px;width:100%;text-align:center;font-family:"Barlow Condensed",sans-serif;font-weight:500;font-size:17px;line-height:24.5px;color:var(--ink)}
  .resource-frame__text .url{display:inline-block;background:var(--paper);padding:0 18px}
  .program-line{left:0;top:917px;width:100%;text-align:center;font-family:"Barlow Condensed",sans-serif;font-weight:500;font-size:17.5px;color:var(--ink);display:flex;justify-content:center;align-items:center;gap:5px}
  .partner-mark{left:102px;top:945px;display:flex;align-items:center;gap:10px}
  .partner-mark__dot{width:50px;height:50px;border-radius:50%;background:#4f9ea3}
  .partner-mark__name{font-family:"Barlow Condensed",sans-serif;font-weight:600;font-size:21px;line-height:22px;color:#3e8f99}
  .funding{left:24px;top:1012px;width:420px;font-family:"Barlow Condensed",sans-serif;font-weight:500;font-size:8.7px;line-height:14.2px;color:var(--ink)}
</style>
</head>
<body>

<section class="card card--front" aria-label="Rack card front">
  <header class="abs front-header">
    <h1>
      <svg class="front-title" viewBox="0 0 466 196" aria-label="Healthy food, healthy brain">
        <text class="front-title__food" x="32" y="96" textLength="420" lengthAdjust="spacingAndGlyphs">HEALTHY FOOD,</text>
        <text class="front-title__brain" x="32" y="180" textLength="412" lengthAdjust="spacingAndGlyphs">HEALTHY BRAIN</text>
      </svg>
    </h1>
    <span class="front-header__pointer"></span>
  </header>

  <p class="abs intro">Everyone slows down as they get older, both in body and mind. Eating healthier food can help your overall health, including brain health. It may also reduce your risk for memory loss and problems thinking.</p>

  <h2 class="abs steps-heading">Healthier steps to protect your brain:</h2>
  <ul class="abs steps">
    <li><svg width="22" height="18" viewBox="0 0 22 18"><path d="M2 10 L8 16 L20 2" fill="none" stroke="#4a2606" stroke-width="3.4" stroke-linecap="round" stroke-linejoin="round"/></svg>Eat more vegetables, fruits, whole grains,<br>and lower-fat milk</li>
    <li><svg width="22" height="18" viewBox="0 0 22 18"><path d="M2 10 L8 16 L20 2" fill="none" stroke="#4a2606" stroke-width="3.4" stroke-linecap="round" stroke-linejoin="round"/></svg>Use less salt and added sugar</li>
    <li><svg width="22" height="18" viewBox="0 0 22 18"><path d="M2 10 L8 16 L20 2" fill="none" stroke="#4a2606" stroke-width="3.4" stroke-linecap="round" stroke-linejoin="round"/></svg>Eat more fish, chicken, turkey, beans, and nuts</li>
    <li><svg width="22" height="18" viewBox="0 0 22 18"><path d="M2 10 L8 16 L20 2" fill="none" stroke="#4a2606" stroke-width="3.4" stroke-linecap="round" stroke-linejoin="round"/></svg>Cut down on bad fats (“saturated” and trans),<br>cholesterol, and red meat</li>
    <li><svg width="22" height="18" viewBox="0 0 22 18"><path d="M2 10 L8 16 L20 2" fill="none" stroke="#4a2606" stroke-width="3.4" stroke-linecap="round" stroke-linejoin="round"/></svg>Buy fresh, not packaged food when you can</li>
    <li><svg width="22" height="18" viewBox="0 0 22 18"><path d="M2 10 L8 16 L20 2" fill="none" stroke="#4a2606" stroke-width="3.4" stroke-linecap="round" stroke-linejoin="round"/></svg>Limit how much alcohol you drink</li>
    <li><svg width="22" height="18" viewBox="0 0 22 18"><path d="M2 10 L8 16 L20 2" fill="none" stroke="#4a2606" stroke-width="3.4" stroke-linecap="round" stroke-linejoin="round"/></svg>Learn your daily calorie needs for your body size</li>
    <li><svg width="22" height="18" viewBox="0 0 22 18"><path d="M2 10 L8 16 L20 2" fill="none" stroke="#4a2606" stroke-width="3.4" stroke-linecap="round" stroke-linejoin="round"/></svg>Take care of your mental and spiritual health to<br>support your physical and brain health</li>
  </ul>

  <p class="abs small-changes">Small changes can make a big difference<br>for better brain health.</p>

  <svg class="abs doctor-band" viewBox="0 0 466 86" preserveAspectRatio="none" aria-hidden="true">
    <path d="M0 6 L120 4 L300 2 L466 5 L466 14 L440 16 L466 20 L466 66 L450 70 L466 74 L466 80 L300 84 L120 82 L0 84 L0 78 L20 74 L0 70 L0 14 L24 12 L0 10 Z" fill="#5f3006"/>
  </svg>
  <p class="abs doctor-band__text">TALK TO YOUR DOCTOR ABOUT MORE STEPS<br>TO HEALTHIER FOOD CHOICES.</p>

  <blockquote class="abs quote">
    <p><span class="quote__mark" style="margin-left:-20px">“</span> Without the elk, salmon, huckleberries, shellfish,<br>and cedar trees we are nobody… <span class="quote__mark">”</span></p>
    <cite>— Marian Tallbrook (Cedar River)</cite>
  </blockquote>

  <div class="abs food-collage" role="img" aria-label="Photo collage of healthy foods: leafy greens, citrus, avocado, berries, nuts, grains, tomatoes, lean meat and salmon"></div>
</section>

<section class="card card--back" aria-label="Rack card back">
  <div class="abs back-header"></div>
  <div class="abs recipe-photo" role="img" aria-label="Photo of salmon, asparagus, peppers and lemon in an open foil packet"></div>
  <h2 class="abs back-title">MAKE THIS AT HOME</h2>
  <p class="abs back-subtitle">Grilled Salmon and Veggie Foil Packets</p>

  <div class="abs ingredients-tag">
    <svg width="122" height="29" viewBox="0 0 122 29" aria-hidden="true"><path d="M10 0 H122 L112 29 H0 Z" fill="#6f9a1d"/></svg>
    <span>Ingredients:</span>
  </div>
  <svg class="abs ingredients-arrow" width="60" height="44" viewBox="0 0 60 44" aria-hidden="true">
    <path d="M2 16 C18 2 44 2 50 30" fill="none" stroke="#6f9a1d" stroke-width="2"/>
    <path d="M44 24 L50 33 L56 24" fill="none" stroke="#6f9a1d" stroke-width="2"/>
  </svg>

  <span class="ingredient" style="left:40px;top:156px">Salmon</span>
  <span class="ingredient" style="left:134px;top:154px">Asparagus</span>
  <span class="ingredient" style="left:272px;top:156px">Onion</span>
  <span class="ingredient" style="left:367px;top:156px">Basil</span>
  <span class="ingredient" style="left:40px;top:190px">Red or Green Peppers<br>(Or any seasonal vegetable)</span>
  <span class="ingredient" style="left:272px;top:190px">Lemon - sliced</span>
  <span class="ingredient" style="left:40px;top:245px">Olive Oil</span>
  <span class="ingredient" style="left:134px;top:245px">Garlic Powder</span>
  <span class="ingredient" style="left:272px;top:243px">Salt and Pepper</span>

  <p class="abs recipe-steps">pieces. Cut salmon into 4-6 oz pieces. Tear tin foil large<br>enough to wrap around salmon &amp; veggies (2 layers). Add<br>veggies and salmon to foil. Drizzle with olive oil, season<br>with salt, pepper, basil, garlic &amp; top with a piece of sliced<br>lemon. Wrap foil tightly around food. Grill at 400 degrees<br>for about 20 minutes.</p>
  <p class="abs careful">Careful opening!</p>

  <div class="abs community-box">
    <p>Food &amp; drink are a source of strength and<br>connection to community. A return to<br>traditional food pathways and eating local,<br>seasonal fresh foods make healthier eating easier.</p>
  </div>

  <h2 class="abs more-info">For More Information<br>About Healthier Eating</h2>

  <p class="abs site-pill">PlateWise Guide |
    <svg width="14" height="14" viewBox="0 0 14 14" aria-hidden="true"><g fill="none" stroke="#fff" stroke-width="1.2"><circle cx="7" cy="7" r="6"/><ellipse cx="7" cy="7" rx="2.6" ry="6"/><path d="M1 7H13M2 4H12M2 10H12"/></g></svg>
    www.platewiseguide.org</p>

  <div class="abs resource-frame"></div>
  <p class="abs resource-frame__text">About Brain Health<br>Northwind Resource Center for Community<br>Brain Health<br><span class="url">www.NorthwindBrainHealth.org</span></p>
  <svg class="abs" style="left:52px;top:901px" width="364" height="2" aria-hidden="true"><path d="M0 1H78M286 1H364" stroke="#2b2b2b" stroke-width="1"/></svg>

  <p class="abs program-line">Harlow Memory Care Program |
    <svg width="13" height="13" viewBox="0 0 14 14" aria-hidden="true"><g fill="none" stroke="#2b2b2b" stroke-width="1.2"><circle cx="7" cy="7" r="6"/><ellipse cx="7" cy="7" rx="2.6" ry="6"/><path d="M1 7H13M2 4H12M2 10H12"/></g></svg>
    www.harlowmemory.org/aging</p>

  <div class="abs partner-mark">
    <span class="partner-mark__dot"></span>
    <span class="partner-mark__name">NORTHWIND BRAIN<br>HEALTH CENTER</span>
  </div>

  <p class="abs funding">This product is supported by the Harlow Health Foundation (HHF) of the Office of Community Wellness (OCW) as part of a financial assistance award totaling $348,711 with 100 percent funded by HHF/OCW. The contents are those of the author(s) and do not necessarily represent the official views of, nor an endorsement, by HHF/OCW, or Public Agencies</p>
</section>

</body>
</html>
```